The Road of Embers trilogy - fantasy fiction

I am republishing my fantasy fiction series, intially published in 2016. I need three book covers for MIRE, THE LANTERN DIMS and ASHEN.
See the files for the initial covers. I particulalry liked the cover of MIRE. Although I don't want to replicate that, I like the colours and general design. I would like a theme through the three covers, either a similar design and different colour scheme, or same colour scheme with a variation on the design. I would prefer the covers to be more abstract thatan the initial covers.

Target Market(s)

Adults

Requirements
Must have
• This is a fantasy fiction series, so I need covers typical of that genre
Nice to have
• I would like a theme through the three covers, either a similar design and different colour scheme, or same colour scheme with a variation on the design. I would prefer the covers to be more abstract thatan the initial covers.

```html
<!DOCTYPE html>
<html lang="en">
<head>
<meta charset="utf-8">
<title>MIRE – Book One of The Road of Embers</title>
<link rel="stylesheet" href="https://fonts.googleapis.com/css2?family=Cinzel+Decorative:wght@700&family=Cinzel:wght@400;600&family=Marcellus&family=Montserrat:wght@400&display=swap">
<style>
  :root {
    --ice-pale: #c9d6e2;
    --snow: #eef2f6;
    --ink-slate: #33495c;
    --ink-spine: #3c4d5c;
    --ink-spine-dark: #2c3944;
    --title-edge: #e3e9f0;
    --text-light: #f3f5f8;
    --photo-frame: #dfe6ee;
  }
  * { margin: 0; padding: 0; box-sizing: border-box; }
  html, body { width: 1200px; height: 821px; overflow: hidden; background: var(--ice-pale); }
  .cover { position: relative; width: 1200px; height: 821px; overflow: hidden; }
  .cover-art {
    position: absolute; inset: 0;
    background:
      radial-gradient(circle at 1099px 84px, #dceaf6 0 58px, rgba(220,234,246,0) 60px),
      radial-gradient(ellipse 420px 300px at 820px 330px, rgba(238,242,246,0.75), rgba(238,242,246,0) 70%),
      radial-gradient(ellipse 500px 200px at 500px 620px, rgba(232,238,244,0.8), rgba(232,238,244,0) 70%),
      linear-gradient(180deg, #35617f 0%, #6f93ae 35%, #b7c9d8 62%, #dfe7ee 85%, #cfdbe6 100%);
  }
  .cover-art::after {
    content: ""; position: absolute; inset: 0;
    background: linear-gradient(90deg, rgba(31,66,92,0.55) 0%, rgba(31,66,92,0.15) 45%, rgba(0,0,0,0) 70%);
  }

  /* Back cover */
  .blurb {
    position: absolute; left: 52px; top: 106px; width: 444px;
    font-family: "Marcellus", serif;
    font-size: 12px; line-height: 17.2px; letter-spacing: 0.2px;
    color: var(--text-light); text-align: center;
  }
  .blurb p + p { margin-top: 17px; }
  .author-photo {
    position: absolute; left: 62px; top: 546px; width: 149px; height: 148px;
    border: 4px solid var(--photo-frame);
    background: linear-gradient(135deg, #8a7a6c, #c5b4a2 50%, #5b5854);
  }
  .author-bio {
    position: absolute; left: 219px; top: 551px; width: 262px;
    font-family: "Montserrat", sans-serif; font-weight: 400;
    font-size: 9.4px; line-height: 15px; letter-spacing: 0.6px;
    color: var(--text-light);
  }
  .author-signature {
    position: absolute; left: 222px; top: 644px; width: 234px; height: 50px;
    background: linear-gradient(90deg, rgba(60,80,100,0.12), rgba(60,80,100,0));
  }

  /* Spine */
  .spine { position: absolute; left: 572px; top: 60px; width: 52px; height: 740px; }
  .spine-line {
    position: absolute; left: 50%;
    writing-mode: vertical-rl; white-space: nowrap;
    transform: translateX(-50%);
    line-height: 1;
  }
  .spine-title {
    top: 8px; font-family: "Cinzel", serif; font-weight: 400;
    font-size: 38px; letter-spacing: 6px; color: var(--snow);
  }
  .spine-series {
    top: 171px; font-family: "Cinzel", serif; font-size: 10.5px; letter-spacing: 2.2px;
    color: var(--ink-spine);
  }
  .spine-author {
    top: 440px; font-family: "Cinzel", serif; font-weight: 400;
    font-size: 23px; letter-spacing: 1.5px; color: var(--ink-spine-dark);
  }

  /* Front cover */
  .front-title {
    position: absolute; left: 706px; top: 104px; width: 446px;
    font-family: "Cinzel Decorative", serif; font-weight: 700;
    font-size: 128px; line-height: 1; letter-spacing: 2px;
    color: var(--ink-slate);
    text-shadow: 4px 3px 0 var(--title-edge);
    text-align: center;
  }
  .front-series {
    position: absolute; left: 760px; top: 244px; width: 320px;
    font-family: "Cinzel", serif; font-size: 15px; line-height: 25px; letter-spacing: 2px;
    color: var(--ink-slate); text-align: center;
  }
  .front-author {
    position: absolute; left: 700px; top: 764px; width: 472px;
    font-family: "Cinzel", serif; font-weight: 600;
    font-size: 35px; line-height: 1; letter-spacing: 1px;
    color: var(--title-edge); text-align: center; white-space: nowrap;
  }
</style>
</head>
<body>
<main class="cover">
  <div class="cover-art" role="img" aria-label="Painted snowy mountain landscape under a full moon, with a sweeping ice arch and two hooded monks walking among jagged dark rocks"></div>

  <section class="back-cover">
    <div class="blurb">
      <p>Jack and Tul are twins separated at birth by dark monks seeking child sacrifices to break down the Weave that separates hell from the world. Tul is taken to the great Monastery of Saint Aldric, set in the mighty snow-covered mountains of northern Velmora to be raised a novice monk, an orphan with no knowledge of his background. Jack grows up in the wilderness of southern Velmora with his two sisters and father.</p>
      <p>Tul stumbles across a prophesy in the monastery library which reveals that a set of twins will be the saviors of Velmora, reversing the chaos that is being unleashed by the blood sacrifice. When they also discover the prophesy, the monks unleash their draugr creatures to find the twins and kill them. Little do they know that one of the twins is under their very noses.</p>
      <p>The twins flee, pursued by the draugr and evil monks. If only they can find each other they might make sense of the increasing chaos that now surrounds them. But, in a world where the separation of good and evil is rapidly fragmenting, Tul and Jack soon find out that no one is really who they seem to be – including themselves!</p>
      <p>Mire is a rich and gripping story of action and adventure, isolation and the strength of family, and the choice between good and evil. Maybe it’s not a fantasy after all …</p>
    </div>
    <div class="author-photo" role="img" aria-label="Portrait photograph of the author"></div>
    <p class="author-bio">Harold Grenwick is the author of the THE ROAD OF EMBERS epic fantasy fiction trilogy: MIRE, THE LANTERN DIMS and ASHEN. The new Dr Nina Carver Murder Mystery series will be out soon: SILENCE ON THE WARD, SHADOWS IN A CLOISTER, and BONES AT THE QUAY.</p>
    <div class="author-signature" role="img" aria-label="Handwritten author signature"></div>
  </section>

  <section class="spine">
    <span class="spine-line spine-title">MIRE</span>
    <span class="spine-line spine-series">BOOK ONE OF THE ROAD OF EMBERS</span>
    <span class="spine-line spine-author">HAROLD GRENWICK</span>
  </section>

  <section class="front-cover">
    <h1 class="front-title">MIRE</h1>
    <p class="front-series">BOOK ONE<br>OF THE ROAD OF EMBERS</p>
    <p class="front-author">HAROLD GRENWICK</p>
  </section>
</main>
</body>
</html>
```